Virtual Background for Lena Crowder's Bayou Velvet Lounge

Seeking a virtual backdrop image for green screen, for live Vistra music performances. The theme is New Orleans style high-end elegant and/or gritty nightclub scene. Should have a sign with the name of the venue "Lena Crowder's Bayou Velvet Lounge" in jazz/soul/blues relevant font. Plus Lena's logo attached below. Ideally proportional so it appears a real as possible singing from the in the venue with people paying attention, or working the crowd walking among seated guests. Lena performed in New Orleans for 7 years before being signed to a label. EPK attached and see website: www.lenacrowder-music.example
Another concept is to incorporate the living room furniture as part of the set, with a green screen behind the couch with bar/club decore that matches the live furniture making it appear that guests and couch are part of a bigger club. See furniture included.

Target Market(s)

Lena's fans are typically 50/50 men and women in age group of 35-70

Font styles to use
Decorative
Script

Requirements
Must have
• "Lena Crowder's Bayouu Velvet Lounge" sign and LC Logo.
Nice to have
• People in seats or standing watching Lena attentively.

```html
<!DOCTYPE html>
<html lang="en">
<head>
<meta charset="utf-8">
<title>Lena Crowder's Bayou Velvet Lounge — Virtual Background</title>
<link rel="stylesheet" href="https://fonts.googleapis.com/css2?family=Rubik:wght@700&family=Sacramento&family=Cinzel:wght@500&display=swap">
<style>
  :root {
    --page-bg: #1d1a1b;
    --night-deep: #0e0618;
    --night-violet: #3a1466;
    --neon-pink: #e43cf0;
    --neon-core: #fff4ff;
    --title-white: #ffffff;
    --crest-gold: #d9b24a;
  }
  * { margin: 0; padding: 0; box-sizing: border-box; }
  html, body {
    width: 1200px;
    height: 1200px;
    overflow: hidden;
    background: var(--page-bg);
  }
  .backdrop {
    position: absolute;
    left: 0;
    top: 200px;
    width: 1200px;
    height: 800px;
    overflow: hidden;
    background: var(--night-deep);
  }
  .club-scene {
    position: absolute;
    inset: 0;
    background:
      radial-gradient(circle at 48% 6%, rgba(255,230,255,0.85) 0, rgba(214,90,255,0.55) 6%, rgba(120,30,200,0) 28%),
      radial-gradient(circle at 22% 10%, rgba(255,120,140,0.7) 0, rgba(214,36,79,0.35) 8%, rgba(214,36,79,0) 24%),
      radial-gradient(ellipse at 70% 30%, rgba(90,150,200,0.35) 0, rgba(90,150,200,0) 30%),
      linear-gradient(180deg, var(--night-violet) 0%, #4b1e86 28%, #22103e 52%, var(--night-deep) 78%, #07030c 100%);
  }
  .venue-sign {
    position: absolute;
    left: 56px;
    top: 110px;
  }
  .venue-sign__owner {
    font-family: "Rubik", sans-serif;
    font-weight: 700;
    font-size: 32px;
    letter-spacing: 1px;
    color: var(--title-white);
    text-transform: uppercase;
    transform: rotate(-3deg);
    transform-origin: left center;
  }
  .venue-sign__name {
    font-family: "Sacramento", cursive;
    font-weight: 400;
    font-size: 112px;
    line-height: 0.85;
    color: var(--neon-core);
    text-shadow:
      0 0 2px var(--neon-pink),
      0 0 5px var(--neon-pink),
      0 0 12px var(--neon-pink),
      0 0 24px var(--neon-pink);
    transform: rotate(-9deg);
    transform-origin: left top;
    margin-top: 62px;
    white-space: nowrap;
  }
  .venue-sign__name span { display: block; }
  .venue-sign__name .line-two { padding-left: 120px; }
  .artist-mark {
    position: absolute;
    right: 40px;
    bottom: 110px;
    display: flex;
    flex-direction: column;
    align-items: center;
    gap: 12px;
  }
  .artist-mark__square {
    width: 80px;
    height: 80px;
    background: var(--crest-gold);
  }
  .artist-mark__name {
    font-family: "Cinzel", serif;
    font-weight: 500;
    font-size: 20px;
    color: var(--crest-gold);
  }
</style>
</head>
<body>
  <main class="backdrop">
    <div class="club-scene" role="img" aria-label="Photo of a crowded nightclub dance floor lit by purple, magenta and red stage lights"></div>

    <header class="venue-sign">
      <p class="venue-sign__owner">Lena Crowder's</p>
      <h1 class="venue-sign__name">
        <span class="line-one">Bayou Velvet</span>
        <span class="line-two">Lounge</span>
      </h1>
    </header>

    <div class="artist-mark">
      <div class="artist-mark__square"></div>
      <p class="artist-mark__name">Lena Crowder</p>
    </div>
  </main>
</body>
</html>
```